Tidewell Shuck-new seafood raw bar restaurant menu

We are a Local Seafood & Raw Bar restaurant that is looking to open in 3 months. I need-Dinner Menu Design, Happy Hour Menu, Cocktail Menu, Brunch Menu, Lunch Menu. I'd like to have you start w/ the dinner menu first then whomever I choose will also do the rest of my menus. The OYSTERDECK by Finnhook menu is the direction im going for as far as font organization. Id like you to give us our own personal touch. Ive also provided a mock menu that a local designer started that can't finish due to timing.

Target Market(s)

mid to high end casual seafood restaurant

Industry/Entity Type

restaurant

Font styles to use
Serif
Sans Serif

Colors
0054AA
0677BA
7BADD7
CADEEF
E8F1F8
0094D4
00A9DD
6FCCEA
C7EBF8
E9F6FB
00AB8E
00BBA5
67D7C9
C6EFE9
E9F9F6

Requirements
Must have
• 11" x 14" size

```html
<!DOCTYPE html>
<html lang="en">
<head>
<meta charset="utf-8">
<title>Tidewell Shuck – Dinner Menu</title>
<link rel="stylesheet" href="https://fonts.googleapis.com/css2?family=Alfa+Slab+One&family=Montserrat:wght@300;400;800&display=swap">
<style>
  :root {
    --bg-deep: #1f4f8c;
    --bg-mid: #3a6a9c;
    --bg-light: #4a78a6;
    --accent: #72cfd9;
    --ink: #f3f6fa;
    --ink-soft: #e4ecf4;
    --rope: #eef3f8;
  }
  * { margin: 0; padding: 0; box-sizing: border-box; }
  html, body { width: 943px; height: 1200px; overflow: hidden; }
  body {
    position: relative;
    background: radial-gradient(ellipse at 40% 40%, var(--bg-light) 0%, var(--bg-mid) 45%, var(--bg-deep) 100%);
    font-family: "Montserrat", sans-serif;
    color: var(--ink);
  }
  .menu-lines { position: absolute; left: 0; top: 0; width: 943px; height: 1200px; }

  .section-title, .raw-bar-title, .raw-bar-sub {
    position: absolute;
    font-family: "Alfa Slab One", serif;
    color: var(--accent);
    font-weight: 400;
    line-height: 1;
    white-space: nowrap;
  }
  .section-title { font-size: 32px; letter-spacing: 0.3px; }
  .raw-bar-title { left: 56px; width: 375px; text-align: center; top: 136px; font-size: 34px; letter-spacing: 0.5px; }
  .raw-bar-sub { left: 56px; width: 375px; text-align: center; top: 174px; font-size: 18.5px; }

  .brand-name {
    position: absolute; left: 213px; top: 82px; width: 60px;
    text-align: center; font-weight: 800;
    font-size: 7px; line-height: 9px; color: var(--ink); letter-spacing: 0.5px;
  }

  .item { position: absolute; line-height: 1; }
  .item-name { font-weight: 800; font-size: 13px; color: var(--ink); white-space: nowrap; }
  .item-desc { font-weight: 300; font-size: 10px; line-height: 12px; color: var(--ink-soft); margin-top: 2px; white-space: nowrap; }
  .price { position: absolute; left: 340px; font-weight: 800; font-size: 10.5px; color: var(--ink); line-height: 1; }
  .price-lg { font-size: 13px; }
  .option { position: absolute; left: 121px; font-size: 10px; font-weight: 300; color: var(--ink-soft); line-height: 1; }

  .signatures .item { left: 567px; }
  .raw-bar .item { left: 121px; }
  .col-left { left: 56px; }
  .col-right { left: 327px; }
  .simple-list .item { left: 667px; }
  .simple-list .item-name { font-size: 12px; }
</style>
</head>
<body>

<svg class="menu-lines" viewBox="0 0 943 1200">
  <path d="M100,37 H387 Q400,37 405,50 Q412,110 431,113 V640 Q412,643 405,700 Q400,712 387,712 H100 Q87,712 82,700 Q75,643 56,640 V113 Q75,110 82,50 Q87,37 100,37 Z"
        fill="none" stroke="#72cfd9" stroke-width="5"/>
  <path d="M104,46 H383 Q392,46 396,56 Q404,114 422,121 V632 Q404,639 396,694 Q392,703 383,703 H104 Q95,703 91,694 Q83,639 65,632 V121 Q83,114 91,56 Q95,46 104,46 Z"
        fill="none" stroke="#72cfd9" stroke-width="1.5"/>
  <g role="img" aria-label="Flourished scroll ornaments in the frame corners">
    <ellipse cx="125" cy="95" rx="48" ry="26" fill="#72cfd9" opacity="0.18"/>
    <ellipse cx="362" cy="95" rx="48" ry="26" fill="#72cfd9" opacity="0.18"/>
    <ellipse cx="125" cy="655" rx="48" ry="26" fill="#72cfd9" opacity="0.18"/>
    <ellipse cx="362" cy="655" rx="48" ry="26" fill="#72cfd9" opacity="0.18"/>
  </g>
  <circle cx="243" cy="91" r="30" fill="none" stroke="#f3f6fa" stroke-width="2"/>
  <g fill="none" stroke="#eef3f8" stroke-width="2.5" stroke-dasharray="2 1.5">
    <path d="M527,113 V667 H820"/>
    <path d="M612,744 V1134 H905"/>
  </g>
</svg>

<div class="brand-name">TIDEWELL SHUCK</div>

<section class="raw-bar">
  <h1 class="raw-bar-title">RAW BAR</h1>
  <h2 class="raw-bar-sub">CHILLED SEAFOOD</h2>

  <div class="item" style="top:220px"><div class="item-name">Oyster chef’s preparation</div></div>
  <div class="price" style="top:220px">22$</div>

  <div class="item" style="top:246px"><div class="item-name">Oyster selection</div></div>
  <div class="option" style="top:263px">House</div><div class="price" style="top:263px">22$</div>
  <div class="option" style="top:276px">East Coast</div><div class="price" style="top:276px">22$</div>
  <div class="option" style="top:289px">Regional</div><div class="price" style="top:289px">22$</div>
  <div class="option" style="top:302px">Accompaniments, top’em</div>

  <div class="item" style="top:325px"><div class="item-name">Seafood Tower</div></div>
  <div class="option" style="top:342px">Small</div><div class="price" style="top:342px">22$</div>
  <div class="option" style="top:355px">Large</div><div class="price" style="top:355px">22$</div>
  <div class="option" style="top:368px">Build Your own</div><div class="price" style="top:368px">22$</div>

  <div class="item" style="top:391px"><div class="item-name">Ceviche</div><div class="item-desc">Citrus, fruit, peppers, onion, cilantro</div></div>
  <div class="price" style="top:391px">22$</div>

  <div class="item" style="top:430px"><div class="item-name">Tuna Poke/crudo</div><div class="item-desc">Ponzu, scallions, ginger, avocado, sesame</div></div>
  <div class="price" style="top:430px">22$</div>

  <div class="item" style="top:469px"><div class="item-name">Scallop Crudo</div><div class="item-desc">Lemon, ginger, chives, olive oil, pine nuts</div></div>
  <div class="price" style="top:469px">22$</div>

  <div class="item" style="top:508px"><div class="item-name">Peel and eat shrimp</div><div class="item-desc">Remoulade, tartar, cocktail</div></div>
  <div class="price price-lg" style="top:508px">22$</div>

  <div class="item" style="top:547px"><div class="item-name">Local Fish Crudo</div><div class="item-desc">Seasonal accompaniments</div></div>
  <div class="price price-lg" style="top:547px">22$</div>

  <div class="item" style="top:587px"><div class="item-name">Cured Salmon</div></div>
  <div class="price price-lg" style="top:587px">22$</div>
</section>

<section class="signatures">
  <h2 class="section-title" style="left:566px;top:84px">SIGNATURES</h2>
  <div class="item" style="top:143px"><div class="item-name">Clam Linguini</div><div class="item-desc">Local Pasta. Local Bacon, peppers, butter, herbs</div></div>
  <div class="item" style="top:182px"><div class="item-name">Vegetable Gnocchi</div><div class="item-desc">Squash, shallots, peas, mushroom, basil,<br>parmesan</div></div>
  <div class="item" style="top:234px"><div class="item-name">Pan Seared Scallops</div><div class="item-desc">Curry, cauliflower, carrots, eggplant, Carolina<br>gold rice</div></div>
  <div class="item" style="top:285px"><div class="item-name">Halibut Gumbo</div><div class="item-desc">Shrimp, scallions, okra garnish</div></div>
  <div class="item" style="top:324px"><div class="item-name">Grilled Steak</div><div class="item-desc">Roasted rainbow carrots, mashed potatoes,<br>ancho demi, chimichurri</div></div>
  <div class="item" style="top:376px"><div class="item-name">Surf and Turf Filet</div><div class="item-desc">Asparagus, baby potatoes, bearnaise, demi<br>Fresh Catch</div></div>
  <div class="item" style="top:427px"><div class="item-name">Crab Legs</div><div class="item-desc">Butter, cocktail, spicy remoulade</div></div>
  <div class="item" style="top:467px"><div class="item-name">Lowcountry Boil</div><div class="item-desc">Shrimp, sausage, corn, potato</div></div>
  <div class="item" style="top:506px"><div class="item-name">Smash Burger</div><div class="item-desc">Spicy “thousand Island”, pickles, house cut<br>fries, LTO</div></div>
  <div class="item" style="top:557px"><div class="item-name">Lobster Roll</div><div class="item-desc">Lots of Lobstah, scallions, celery, house fries</div></div>
  <div class="item" style="top:596px"><div class="item-name">Fish Sandwich</div><div class="item-desc">Double stacked halibut, pickled carrots,<br>Lemon/caper/dill aioli, lettuce, tomato</div></div>
</section>

<section class="smaller">
  <h2 class="section-title" style="left:229px;top:766px">SMALLER</h2>
  <div class="item col-left" style="top:838px"><div class="item-name">Fried Shrimp</div><div class="item-desc">Remoulade</div></div>
  <div class="item col-left" style="top:877px"><div class="item-name">Mussels</div><div class="item-desc">Local bacon, shallot, garlic, tomato, spicy<br>herb butter</div></div>
  <div class="item col-left" style="top:926px"><div class="item-name">Roasted Oysters</div><div class="item-desc">½ dozen, Choice of Rockefeller, Bienville,<br>Tidewell special</div></div>
  <div class="item col-left" style="top:975px"><div class="item-name">Shrimp and Grits</div><div class="item-desc">Local andouille, roasted peppers, garlic,<br>shallot, charred tomato</div></div>
  <div class="item col-left" style="top:1024px"><div class="item-name">Crab Mac’n cheese</div><div class="item-desc">Cheddar, fontina, cotija, local pasta shells</div></div>
  <div class="item col-left" style="top:1073px"><div class="item-name">Shrimp Remoulade</div><div class="item-desc">Avocado, fried green tomato</div></div>

  <div class="item col-right" style="top:838px"><div class="item-name">Pumpkin Risotto</div><div class="item-desc">Herbs, dried cherry, local mushrooms</div></div>
  <div class="item col-right" style="top:877px"><div class="item-name">Caeser</div><div class="item-desc">Baby gem lettuce, parmesan</div></div>
  <div class="item col-right" style="top:926px"><div class="item-name">Greenrow crisp greens salad</div><div class="item-desc">Fig, goat cheese, spiced pepitos, sour cherry<br>vinaigrette</div></div>
  <div class="item col-right" style="top:975px"><div class="item-name">Clam Chowder</div><div class="item-desc">New England style</div></div>
  <div class="item col-right" style="top:1024px"><div class="item-name">Baja Fish Tacos</div><div class="item-desc">Slaw, cilantro, lime</div></div>
  <div class="item col-right" style="top:1073px"><div class="item-name">Steak Taco</div><div class="item-desc">Mojo, dried chili salsa, pickled onion, cotija</div></div>
</section>

<section class="simple-list kids">
  <h2 class="section-title" style="left:664px;top:742px">KIDS MENU</h2>
  <div class="item" style="top:803px"><div class="item-name">Chicken tenders</div></div>
  <div class="item" style="top:837px"><div class="item-name">Mac n cheese</div></div>
  <div class="item" style="top:872px"><div class="item-name">Fried Fish</div></div>
  <div class="item" style="top:906px"><div class="item-name">Fried Shrimp</div></div>
</section>

<section class="simple-list desserts">
  <h2 class="section-title" style="left:664px;top:959px">DESSERTS</h2>
  <div class="item" style="top:1021px"><div class="item-name">Chocolate</div></div>
  <div class="item" style="top:1055px"><div class="item-name">Raspberry</div></div>
  <div class="item" style="top:1090px"><div class="item-name">blue</div></div>
</section>

</body>
</html>
```